CareWillow Brand Standards and Core Values

I would like to have frameable posters made up for each office using our brand standards. I would like the posters to include:Our Vision Statement:We are transforming the healthcare staffing and homecare industry with our people-oriented, world-class team. Clients choose us, and develop lasting bonds with our team because of our impeccably high standards and our reputation for always remembering this is, first and foremost, a people business. We consistently go the extra mile to ensure our nurses and those being cared for are at all times, treated with dignity and respect. We hold ourselves and those we work with to the highest possible standards. We consistently deliver what we promise, and whenever possible, even more. Our Mission Statement:We go above and beyond to ensure our clients receive the right care and the right people at the right time. Our rigorous recruitment standards result in strong caregivers who are trusted for their expertise, experience and compassion. Our Values:Through our genuine caring and compassion, we are committed to honor all with whom we interact. We are grounded in our faith and dedicated to working together as a family that consistently and passionately lives our values. Compassion Integrity and honesty Faith Decisive action Constant and never-ending improvement Personal ownership Excellence Positive attitude Passion RespectWho we are:We are friendly, servant leaders who have a sense of urgency to meet the needs of our nurses and clients. We prioritize personal relationships with genuine caring and compassion. We inspire others through our passion and energy.Our main colors are: HEX# 5C80DE, HEX# BDE080, HEX# 8C8C8Caccent colors are: HEX# 95D6E3, HEX# AD59AB, HEX# 002E57

Target Market(s)

office employee inspiration

Font styles to use
Other font styles liked:
• Verdana

Colors

Designer to choose colors to be used in the design.

Requirements
Must have
• the core values listed in description
Nice to have
• colors given in description, something fun and inspiring for office employees to help motivate them !
Should not have
• colors that are not company colors. I have listed HEX codes in description

```html
<!DOCTYPE html>
<html lang="en">
<head>
<meta charset="utf-8">
<title>CareWillow — Vision and Mission</title>
<link href="https://fonts.googleapis.com/css2?family=Open+Sans:wght@600;700;800&display=swap" rel="stylesheet">
<style>
  :root{
    --sky:#6079bd;
    --panel:#4d6aa6;
    --panel-edge:#3b5688;
    --crowd:#46639e;
    --green:#bddc80;
    --aqua:#95d6e3;
    --plum:#ad59ab;
    --navy:#172e57;
    --ink:#1a2e50;
    --white:#ffffff;
  }
  *{margin:0;padding:0;box-sizing:border-box}
  html,body{width:900px;height:1200px;overflow:hidden}
  body{background:var(--sky);font-family:"Open Sans",Verdana,sans-serif;position:relative}
  .stripe{position:absolute;left:0;width:900px;display:flex}
  .stripe span{display:block;height:100%}
  .stripe-top{top:0;height:21px}
  .stripe-bottom{top:1180px;height:20px}
  .c-green{background:var(--green)} .c-plum{background:var(--plum)}
  .c-navy{background:var(--navy)} .c-aqua{background:var(--aqua)}
  .crowd{position:absolute;left:0;width:900px;background:var(--crowd)}
  .crowd-top{top:228px;height:108px}
  .crowd-bottom{top:1090px;height:90px}
  .vision-bubble{position:absolute;left:0;top:0;width:900px;height:300px}
  .vision-text{position:absolute;left:139px;top:38px;width:614px;text-align:center;color:var(--white)}
  .vision-title{font-size:31px;font-weight:800;line-height:1;margin-top:24px;letter-spacing:.5px}
  .vision-line{font-size:20px;font-weight:800;line-height:26px;margin-top:4px}
  .vision-accent{font-size:48px;font-weight:800;line-height:1;margin-top:2px}
  .ribbon{position:absolute;left:0;width:900px}
  .ribbon svg{position:absolute;left:0;top:0}
  .ribbon p{position:absolute;left:41px;width:780px;color:var(--ink);font-weight:700;font-size:16.6px;line-height:21px}
  .mission{position:absolute;left:31px;top:753px;width:847px;height:336px;background:var(--panel);border:8px solid var(--panel-edge);border-radius:22px}
  .mission h2{color:var(--white);font-weight:800;font-size:31px;text-align:center;margin-top:26px;letter-spacing:.5px}
  .mission p{color:var(--white);font-weight:700;font-size:15.2px;line-height:21.6px;text-align:justify;margin:13px 37px 0 46px}
</style>
</head>
<body>
  <div class="stripe stripe-top">
    <span class="c-green" style="width:149px"></span><span class="c-plum" style="width:129px"></span><span class="c-navy" style="width:153px"></span><span class="c-aqua" style="width:151px"></span><span class="c-plum" style="width:128px"></span><span class="c-green" style="width:190px"></span>
  </div>

  <div class="crowd crowd-top" role="img" aria-label="Row of simple team member silhouettes"></div>

  <svg class="vision-bubble" viewBox="0 0 900 300" aria-hidden="true">
    <path d="M160 41 H732 Q750 41 750 59 V210 Q750 228 732 228 H612 Q612 262 639 288 Q585 272 535 228 H160 Q142 228 142 210 V59 Q142 41 160 41 Z" fill="var(--panel)" stroke="var(--panel-edge)" stroke-width="7" stroke-linejoin="round"/>
  </svg>
  <div class="vision-text">
    <h1 class="vision-title">OUR VISION</h1>
    <div class="vision-line">Transforming the healthcare staffing<br>and homecare industry with our people-oriented,</div>
    <div class="vision-accent">world-class team!</div>
  </div>

  <div class="ribbon" style="top:330px;height:121px">
    <svg width="900" height="121" aria-hidden="true">
      <polygon points="0,0 862,0 818,66 862,121 0,121" fill="var(--green)"/>
      <line x1="4" y1="12" x2="842" y2="12" stroke="var(--white)" stroke-width="2.5" stroke-dasharray="8 7"/>
      <line x1="4" y1="108" x2="846" y2="108" stroke="var(--white)" stroke-width="2.5" stroke-dasharray="8 7"/>
    </svg>
    <p style="top:30px">Clients choose us, and develop lasting bonds with our team because of our impeccably high standards and our reputation for always remembering this is, first and foremost, a people business.</p>
  </div>

  <div class="ribbon" style="top:472px;height:120px">
    <svg width="900" height="120" aria-hidden="true">
      <polygon points="0,0 862,0 818,66 862,120 0,120" fill="var(--aqua)"/>
      <line x1="4" y1="12" x2="846" y2="12" stroke="var(--white)" stroke-width="2.5" stroke-dasharray="8 7"/>
      <line x1="4" y1="107" x2="846" y2="107" stroke="var(--white)" stroke-width="2.5" stroke-dasharray="8 7"/>
    </svg>
    <p style="top:38px">We consistently go the extra mile to ensure our nurses and those<br>being cared for are at all times, treated with dignity and respect.</p>
  </div>

  <div class="ribbon" style="top:616px;height:120px">
    <svg width="900" height="120" aria-hidden="true">
      <polygon points="0,0 862,0 818,66 862,120 0,120" fill="var(--green)"/>
      <line x1="4" y1="15" x2="846" y2="15" stroke="var(--white)" stroke-width="2.5" stroke-dasharray="8 7"/>
      <line x1="4" y1="110" x2="846" y2="110" stroke="var(--white)" stroke-width="2.5" stroke-dasharray="8 7"/>
    </svg>
    <p style="top:36px">We hold ourselves and those we work with to the highest possible standards.<br>We consistently deliver what we promise, and whenever possible, even more</p>
  </div>

  <section class="mission">
    <h2>OUR MISSION STATEMENT</h2>
    <p>We go above and beyond to ensure our clients receive the right care and the right people at the right time. Our rigorous recruitment standards result in strong caregivers who are trusted for their expertise, experience and compassion. Our Values:Through our genuine caring and compassion, we are committed to honor all with whom we interact.<br>We are grounded in our faith and dedicated to working together as a family that consistently and passionately lives our values. Compassion Integrity and honesty Faith Decisive action Constant and never-ending improvement Personal ownership Excellence Positive attitude Passion RespectWho we are:We are friendly, servant leaders who have a sense of urgency to meet the needs of our nurses and clients. We prioritize personal relationships with genuine caring and compassion. We inspire others through our passion and energy.</p>
  </section>

  <div class="crowd crowd-bottom" role="img" aria-label="Row of simple team member silhouettes"></div>

  <div class="stripe stripe-bottom">
    <span class="c-green" style="width:154px"></span><span class="c-plum" style="width:129px"></span><span class="c-navy" style="width:152px"></span><span class="c-aqua" style="width:153px"></span><span class="c-plum" style="width:127px"></span><span class="c-green" style="width:185px"></span>
  </div>
</body>
</html>
```